Business Card for Veltrava
Veltrava
Project: Business Card for Veltrava
Business Card for Veltrava - Information Technology
Creative Brief
Professional
Dana Holbrook
7312 Ferncliff Drive #210 Marlow Bend, NC 28614
919-486-3071 ext. 214
dana.holbrook@veltrava.example
www.veltrava.example
Please incorporate uploaded logo in your design
Logo + Veltrava or designs' ideas

```html
<!DOCTYPE html>
<html lang="en">
<head>
<meta charset="utf-8">
<title>Veltrava Business Card</title>
<link rel="stylesheet" href="https://fonts.googleapis.com/css2?family=Montserrat:wght@400;600;700&display=swap">
<style>
  :root {
    --bg: #e9eaed;
    --card: #ffffff;
    --blue-deep: #1d2a9c;
    --blue: #2e46c8;
    --blue-light: #6f86e6;
    --navy: #1b2466;
    --ink: #3c4a8a;
    --grey: #6a7080;
  }
  * { margin: 0; padding: 0; box-sizing: border-box; }
  html, body { width: 1200px; height: 864px; overflow: hidden; }
  body {
    background: var(--bg);
    font-family: "Montserrat", Arial, sans-serif;
    position: relative;
  }
  .card {
    position: absolute;
    left: 290px;
    width: 620px;
    height: 354px;
    background: var(--card);
    border-radius: 22px;
    box-shadow: 0 6px 18px rgba(20, 25, 60, 0.18);
    overflow: hidden;
  }
  .card--back { top: 50px; }
  .card--front { top: 460px; }

  .back-mark {
    position: absolute;
    top: 128px; left: 0; right: 0;
    display: flex; align-items: center; justify-content: center; gap: 14px;
  }
  .mark-dot {
    width: 44px; height: 44px; border-radius: 50%;
    background: var(--blue);
  }
  .brand-name {
    font-weight: 700;
    color: var(--navy);
    font-size: 30px;
    letter-spacing: 1px;
  }
  .back-web {
    position: absolute;
    top: 210px; left: 0; right: 0;
    text-align: center;
    font-size: 11px;
    letter-spacing: 5px;
    color: var(--grey);
  }

  .swoosh { position: absolute; inset: 0; }
  .holder-name {
    position: absolute;
    top: 34px; right: 36px;
    font-size: 14px;
    font-weight: 600;
    letter-spacing: 3px;
    text-transform: uppercase;
    color: var(--blue);
  }
  .front-mark {
    position: absolute;
    left: 40px; top: 190px;
    display: flex; align-items: center; gap: 10px;
  }
  .front-mark .mark-dot { width: 34px; height: 34px; }
  .front-mark .brand-name { font-size: 22px; }
  .contact {
    position: absolute;
    left: 42px; top: 236px;
    list-style: none;
    font-size: 10.5px;
    line-height: 17px;
    color: var(--ink);
  }
  .contact li { display: flex; align-items: center; gap: 8px; }
  .contact svg { width: 11px; height: 11px; flex: none; }
</style>
</head>
<body>
  <section class="card card--back" aria-label="Card back">
    <div class="back-mark">
      <span class="mark-dot"></span>
      <span class="brand-name">Veltrava</span>
    </div>
    <p class="back-web">www.veltrava.example</p>
  </section>

  <section class="card card--front" aria-label="Card front">
    <svg class="swoosh" viewBox="0 0 620 354" preserveAspectRatio="none" aria-hidden="true">
      <defs>
        <linearGradient id="bandFill" x1="0" y1="0" x2="1" y2="1">
          <stop offset="0" stop-color="var(--blue-deep)"/>
          <stop offset="1" stop-color="var(--blue)"/>
        </linearGradient>
      </defs>
      <path d="M0 0 H400 C330 60 250 110 140 130 C80 140 30 150 0 170 Z" fill="url(#bandFill)"/>
      <path d="M400 0 C330 60 250 110 140 130 C80 140 30 150 0 170" fill="none" stroke="var(--blue-light)" stroke-width="3"/>
      <path d="M430 0 C360 70 270 125 150 146 C90 156 40 166 0 186" fill="none" stroke="var(--blue)" stroke-width="2"/>
    </svg>

    <p class="holder-name">Dana Holbrook</p>

    <div class="front-mark">
      <span class="mark-dot"></span>
      <span class="brand-name">Veltrava</span>
    </div>

    <ul class="contact">
      <li><svg viewBox="0 0 12 12"><path d="M6 1a3.5 3.5 0 0 0-3.5 3.5C2.5 7.5 6 11 6 11s3.5-3.5 3.5-6.5A3.5 3.5 0 0 0 6 1zm0 5a1.4 1.4 0 1 1 0-2.8A1.4 1.4 0 0 1 6 6z" fill="var(--blue)"/></svg>7312 Ferncliff Drive #210</li>
      <li><svg viewBox="0 0 12 12"></svg>Marlow Bend, NC 28614</li>
      <li><svg viewBox="0 0 12 12"><circle cx="6" cy="6" r="5.5" fill="var(--blue)"/><path d="M4 3.5l1 1-.6.9c.4.9 1 1.5 1.9 1.9l.9-.6 1 1-.7.9C5.6 8.4 3.6 6.4 3.4 4.2z" fill="#fff"/></svg>919-486-3071 ext. 214</li>
      <li><svg viewBox="0 0 12 12"><circle cx="6" cy="6" r="5.5" fill="var(--blue)"/><rect x="3.5" y="3" width="5" height="6" fill="#fff"/></svg>919-486-3079</li>
      <li><svg viewBox="0 0 12 12"><circle cx="6" cy="6" r="5.5" fill="var(--blue)"/><path d="M3 4h6v4H3z M3 4l3 2.2L9 4" fill="none" stroke="#fff" stroke-width="0.9"/></svg>dana.holbrook@veltrava.example</li>
      <li><svg viewBox="0 0 12 12"><circle cx="6" cy="6" r="5.5" fill="var(--blue)"/><circle cx="6" cy="6" r="2.8" fill="none" stroke="#fff" stroke-width="0.9"/><path d="M3.2 6h5.6M6 3.2v5.6" stroke="#fff" stroke-width="0.7"/></svg>www.veltrava.example</li>
    </ul>
  </section>
</body>
</html>
```